Business card for my new company (Accounting firm)

I need a business card for my new business Corvel Advisory and Finance SA. Our services are accounting, tax, audit and financial management. Our customers are small companies, start-ups and new companies. The final design has to show financial security, trust and growth. Please find our logo attached to the business card. Text for the business card: Corvel Advisory and Finance SA Tomas de Valbueno Director and Founder Certified Accountant Tel. 022 418 27 53 tv@corvelconseil.ch www.corvelconseil.ch Rue des Verniquets 14 1201 Geneva
Target Market(s)
Our customers are small companies, start-ups and new companies.
Industry/Entity Type
Finance And Accounting
Contact Information for Business Card
Corvel Conseil et Finance SA
Tomas de Valbueno
Directeur et Fondateur
Expert-comptable diplômé
Tél. 022 418 27 53
tv@corvelconseil.ch
www.corvelconseil.ch
Rue des Verniquets 14
1201 Genève

```html
<!DOCTYPE html>
<html lang="fr">
<head>
<meta charset="utf-8">
<title>Corvel Conseil et Finance SA – Carte de visite</title>
<link href="https://fonts.googleapis.com/css2?family=Roboto:wght@400;500;700&display=swap" rel="stylesheet">
<style>
  :root {
    --bg: #e4e5e7;
    --card: #ffffff;
    --blue-dark: #145a8c;
    --blue-mid: #1f7ab8;
    --blue-light: #2a9fd6;
    --charcoal: #333538;
    --text: #3a3c40;
  }
  * { margin: 0; padding: 0; box-sizing: border-box; }
  html, body {
    width: 1200px; height: 726px; overflow: hidden;
    background: var(--bg);
    font-family: "Roboto", Arial, sans-serif;
  }
  .sheet {
    position: relative; width: 1200px; height: 726px;
    display: flex; align-items: center; justify-content: center; gap: 60px;
  }
  .card {
    position: relative; width: 510px; height: 310px;
    background: var(--card); overflow: hidden;
    box-shadow: 0 6px 18px rgba(0,0,0,.12);
  }
  .card svg.decor { position: absolute; inset: 0; width: 100%; height: 100%; }

  /* wordmark */
  .wordmark { position: absolute; display: flex; align-items: center; gap: 12px; }
  .wordmark-square { width: 34px; height: 34px; background: var(--blue-mid); }
  .wordmark-name {
    color: var(--charcoal); font-weight: 500; font-size: 22px;
    letter-spacing: .04em; line-height: 1.15;
  }

  /* front */
  .card-front .wordmark { left: 50%; top: 112px; transform: translateX(-50%); }

  /* back */
  .card-back .wordmark { left: 28px; bottom: 40px; }
  .card-back .wordmark-name { font-size: 19px; }
  .identity {
    position: absolute; right: 26px; top: 22px; text-align: right; color: #fff;
  }
  .identity-name { font-weight: 700; font-size: 19px; margin-bottom: 4px; }
  .identity-role { font-size: 11.5px; line-height: 1.35; }
  .contact {
    position: absolute; right: 22px; top: 148px; text-align: right;
    color: var(--text); font-size: 12.5px; line-height: 1.5;
  }
  .contact-address { margin-bottom: 10px; }
  .contact-line { display: flex; justify-content: flex-end; align-items: center; gap: 8px; }
  .contact-icon { width: 12px; height: 12px; fill: var(--blue-mid); }
</style>
</head>
<body>
<main class="sheet">

  <section class="card card-front" aria-label="Recto">
    <svg class="decor" viewBox="0 0 510 310" preserveAspectRatio="none" aria-hidden="true">
      <rect x="0" y="262" width="510" height="6" fill="var(--blue-light)"/>
      <rect x="0" y="268" width="510" height="5" fill="var(--blue-dark)"/>
    </svg>
    <div class="wordmark">
      <span class="wordmark-square"></span>
      <span class="wordmark-name">Corvel Conseil<br>et Finance</span>
    </div>
  </section>

  <section class="card card-back" aria-label="Verso">
    <svg class="decor" viewBox="0 0 510 310" preserveAspectRatio="none" aria-hidden="true">
      <defs>
        <linearGradient id="bandBlue" x1="0" y1="0" x2="1" y2="0">
          <stop offset="0" stop-color="var(--blue-light)"/>
          <stop offset="1" stop-color="var(--blue-dark)"/>
        </linearGradient>
      </defs>
      <path d="M0,0 H510 V92 C430,96 350,92 270,110 C180,130 90,170 0,190 Z" fill="url(#bandBlue)"/>
      <path d="M0,206 C100,178 190,138 280,122 C360,108 440,108 510,104 V112 C440,116 370,118 290,132 C200,148 110,186 0,216 Z" fill="var(--charcoal)"/>
    </svg>

    <div class="identity">
      <p class="identity-name">Tomas de Valbueno</p>
      <p class="identity-role">Directeur et Fondateur<br>Expert-comptable diplômé</p>
    </div>

    <div class="contact">
      <p class="contact-address">Rue des Verniquets 14<br>1201 Genève</p>
      <p class="contact-line">022 418 27 53
        <svg class="contact-icon" viewBox="0 0 24 24" aria-label="Téléphone"><path d="M6.6 10.8a15 15 0 0 0 6.6 6.6l2.2-2.2a1 1 0 0 1 1-.25 11.4 11.4 0 0 0 3.6.57 1 1 0 0 1 1 1V20a1 1 0 0 1-1 1A17 17 0 0 1 3 4a1 1 0 0 1 1-1h3.5a1 1 0 0 1 1 1c0 1.25.2 2.45.57 3.6a1 1 0 0 1-.25 1z"/></svg>
      </p>
      <p class="contact-line">tv@corvelconseil.ch
        <svg class="contact-icon" viewBox="0 0 24 24" aria-label="E-mail"><path d="M2 5h20v14H2z M2 5l10 8 10-8" fill="none" stroke="var(--blue-mid)" stroke-width="2.4"/></svg>
      </p>
      <p class="contact-line">www.corvelconseil.ch
        <svg class="contact-icon" viewBox="0 0 24 24" aria-label="Site web"><circle cx="12" cy="12" r="10" fill="none" stroke="var(--blue-mid)" stroke-width="2.4"/><path d="M2 12h20M12 2c3 3 3 17 0 20M12 2c-3 3-3 17 0 20" fill="none" stroke="var(--blue-mid)" stroke-width="1.8"/></svg>
      </p>
    </div>

    <div class="wordmark">
      <span class="wordmark-square"></span>
      <span class="wordmark-name">Corvel Conseil<br>et Finance</span>
    </div>
  </section>

</main>
</body>
</html>
```